Mr Pellowes Yard Works flyer for newsletter

I need a professional looking flyer design for my company Mr Pellowes Yard Works based in New Braunfels, TX to boost sales. Must include the following: Lawn service starting at $40 (mowing, edging, leaf blowing) Tree trimming starting at $125. Other services-mulching, shrub trimming, aeration, flower bed maintenance, Fall/spring clean up. Serving New Braunfels and surrounding areas. To set up and estimate please call 512 555 0143 or email mrpellowesyard@example-mail.net

Industry/Entity Type

Landscaping

Font styles to use
Serif

Colors

Designer to choose colors to be used in the design.

Requirements
Must have
• Phone number 512 555 0143
• Email mrpellowesyard@example-mail.net

```html
<!DOCTYPE html>
<html lang="en">
<head>
<meta charset="utf-8">
<title>Mr Pellowes Yard Works – Flyer</title>
<link href="https://fonts.googleapis.com/css2?family=Zilla+Slab:wght@700&family=Raleway:wght@300;400&family=Oswald:wght@500&family=Montserrat:wght@700;800&family=Abril+Fatface&display=swap" rel="stylesheet">
<style>
  :root {
    --green: #1b7a3a;
    --green-deep: #17693a;
    --yellow: #f6cf05;
    --white: #ffffff;
    --grass: #5da52f;
    --grass-dark: #3f7d22;
    --mower-red: #d8343a;
    --fence: #8a5a3a;
    --leaf: #d9922e;
  }
  * { margin: 0; padding: 0; box-sizing: border-box; }
  html, body { width: 917px; height: 1200px; overflow: hidden; background: var(--white); }
  .flyer { position: relative; width: 917px; height: 1200px; background: var(--white); overflow: hidden; }

  .photo-column {
    position: absolute; inset: 0;
    clip-path: polygon(315px 0, 917px 0, 917px 550px, 531px 550px);
  }
  .photo { position: absolute; left: 0; width: 917px; }
  .photo-mower-ride {
    top: 0; height: 183px;
    background:
      radial-gradient(ellipse 170px 110px at 700px 95px, rgba(214,52,46,0.95), rgba(214,52,46,0) 100%),
      radial-gradient(ellipse 130px 80px at 860px 60px, rgba(206,48,44,0.9), rgba(206,48,44,0) 100%),
      linear-gradient(180deg, rgba(138,90,58,0.85) 0%, rgba(138,90,58,0.4) 55%, rgba(93,165,47,0) 70%),
      linear-gradient(180deg, #6f9a3c 0%, var(--grass) 100%);
  }
  .photo-leaves {
    top: 183px; height: 184px;
    background:
      radial-gradient(ellipse 200px 120px at 520px 120px, rgba(217,146,46,0.95), rgba(217,146,46,0) 100%),
      radial-gradient(ellipse 150px 90px at 660px 60px, rgba(230,170,60,0.7), rgba(230,170,60,0) 100%),
      linear-gradient(180deg, #4c8a2a 0%, #78b13d 100%);
  }
  .photo-hedge {
    top: 367px; height: 183px;
    background:
      radial-gradient(ellipse 120px 90px at 880px 100px, rgba(150,170,185,0.8), rgba(150,170,185,0) 100%),
      radial-gradient(ellipse 220px 80px at 600px 30px, rgba(190,200,90,0.6), rgba(190,200,90,0) 100%),
      linear-gradient(180deg, #4b8a2b 0%, #3a7424 100%);
  }

  .brand-title {
    position: absolute; left: 58px; top: 44px;
    font-family: "Zilla Slab", serif; font-weight: 700;
    font-size: 56px; line-height: 58px; letter-spacing: -1px;
  }
  .brand-title .line-1 { color: var(--green); display: block; }
  .brand-title .line-2 { color: var(--yellow); display: block; }

  .offer { position: absolute; text-align: right; font-family: "Raleway", sans-serif; font-weight: 400; color: var(--green); font-size: 46px; line-height: 40px; letter-spacing: 0.5px; }
  .offer-lawn { right: 588px; top: 186px; }
  .offer-tree { right: 535px; top: 378px; }
  .offer-note { display: block; margin-top: 8px; font-family: "Oswald", sans-serif; font-weight: 500; font-size: 15px; line-height: 18px; color: var(--yellow); letter-spacing: 0.5px; }

  .price-badge {
    position: absolute; width: 166px; height: 166px; border-radius: 50%;
    background: var(--white); display: flex; align-items: center; justify-content: center;
    box-shadow: 0 2px 6px rgba(0,0,0,0.15);
  }
  .price-badge .disc {
    width: 132px; height: 132px; border-radius: 50%; background: var(--green-deep);
    display: flex; flex-direction: column; align-items: center; justify-content: center; color: var(--yellow);
  }
  .price-badge .at { font-family: "Raleway", sans-serif; font-weight: 400; color: var(--white); font-size: 24px; line-height: 24px; }
  .price-badge .amount { font-family: "Abril Fatface", serif; font-size: 52px; line-height: 58px; }
  .price-lawn { left: 348px; top: 175px; }
  .price-tree { left: 402px; top: 357px; }

  .photo-push-mower {
    position: absolute; left: 0; top: 550px; width: 917px; height: 465px;
    background:
      radial-gradient(ellipse 230px 260px at 760px 210px, rgba(216,52,58,1), rgba(216,52,58,0.9) 60%, rgba(216,52,58,0) 100%),
      radial-gradient(ellipse 80px 130px at 440px 120px, rgba(60,60,60,0.55), rgba(60,60,60,0) 100%),
      radial-gradient(ellipse 90px 140px at 850px 380px, rgba(235,235,230,0.7), rgba(235,235,230,0) 100%),
      linear-gradient(180deg, #6db33a 0%, var(--grass) 50%, var(--grass-dark) 100%);
  }

  .ribbon {
    position: absolute; left: 0; background: var(--green);
    font-family: "Montserrat", sans-serif; font-weight: 800; color: var(--yellow);
    display: flex; align-items: center; white-space: nowrap;
  }
  .ribbon-services { top: 598px; height: 70px; width: 455px; padding-left: 67px; font-size: 28px; clip-path: polygon(0 0, 425px 0, 455px 70px, 0 70px); }
  .ribbon-estimate { top: 983px; height: 69px; width: 561px; padding-left: 58px; font-size: 29px; clip-path: polygon(0 0, 526px 0, 561px 69px, 0 69px); }

  .services-list {
    position: absolute; left: 67px; top: 676px;
    font-family: "Montserrat", sans-serif; font-weight: 700; color: var(--white);
    font-size: 28px; line-height: 48px; letter-spacing: -0.5px;
    text-shadow: 1px 2px 3px rgba(0,0,0,0.55);
  }

  .contact { position: absolute; left: 0; top: 1066px; width: 560px; font-family: "Raleway", sans-serif; font-size: 27px; line-height: 34px; }
  .contact p { white-space: nowrap; }
  .contact .label { color: var(--yellow); font-weight: 300; }
  .contact .value { color: var(--green); font-family: "Montserrat", sans-serif; font-weight: 700; font-size: 26px; }
  .contact .row-call { padding-left: 133px; }
  .contact .row-or { padding-left: 274px; }
  .contact .row-email { padding-left: 63px; font-size: 24px; }
  .contact .row-email .value { font-size: 21px; letter-spacing: -0.2px; }

  .brand-mark { position: absolute; left: 577px; top: 1080px; display: flex; align-items: center; gap: 10px; white-space: nowrap; }
  .brand-mark .dot { width: 14px; height: 14px; border-radius: 50%; background: var(--yellow); }
  .brand-mark .name { font-family: "Montserrat", sans-serif; font-weight: 700; font-size: 32px; color: var(--green); }
</style>
</head>
<body>
<main class="flyer">
  <div class="photo-column">
    <div class="photo photo-mower-ride" role="img" aria-label="Red riding mower cutting a lawn beside a wooden fence"></div>
    <div class="photo photo-leaves" role="img" aria-label="Leaf blower clearing autumn leaves off green grass"></div>
    <div class="photo photo-hedge" role="img" aria-label="Gloved hands trimming a hedge with shears"></div>
  </div>

  <h1 class="brand-title"><span class="line-1">Mr Pellowes</span><span class="line-2">Yard Works</span></h1>

  <p class="offer offer-lawn">LAWN<br>SERVICE<br>STARTING<span class="offer-note">(MOWING, EDGING, LEAF BLOWING)</span></p>
  <div class="price-badge price-lawn"><div class="disc"><span class="at">AT</span><span class="amount">$40</span></div></div>

  <p class="offer offer-tree">TREE<br>TRIMMING<br>STARTING</p>
  <div class="price-badge price-tree"><div class="disc"><span class="at">AT</span><span class="amount">$125</span></div></div>

  <div class="photo-push-mower" role="img" aria-label="Red push lawn mower on freshly cut grass"></div>

  <h2 class="ribbon ribbon-services">OTHER SERVICES:</h2>
  <p class="services-list">Mulching, Shrub<br>Trimming, Aeration,<br>Flower Bed Maintenance,<br>Fall/spring Clean Up.<br>Serving New Braunfels<br>And Surrounding Areas.</p>

  <h2 class="ribbon ribbon-estimate">TO SET UP AND ESTIMATE</h2>

  <div class="contact">
    <p class="row-call"><span class="label">Please Call: </span><span class="value">512 555 0143</span></p>
    <p class="row-or"><span class="label">Or</span></p>
    <p class="row-email"><span class="label">Email: </span><span class="value">mrpellowesyard@example-mail.net</span></p>
  </div>

  <div class="brand-mark"><span class="dot"></span><span class="name">MR PELLOWES</span></div>
</main>
</body>
</html>
```